I need a flyer made , the flyer can be one page or two pages or three pages . I will be posting this on Instagram and social media platforms. I am a luxury home builder , I am looking to hire a construction project manager . Below are some examples and ideas what can be on the flyer

We’re looking for a construction project manager who’s passionate about building luxury homes at the highest standards
We’re hiring construction project manager
* Experience 5+ years in residential project management with a strong portfolio of completed homes.
* location : Bergen County NJ
* excellent leadership skills, leads teams with confidence and clarity
* communicates seamlessly with architects , engineers, designers and clients
*knows how to manage budgets and timelines without compromising quality
*solves problems with a positive solution first mindset
* pays attention to every detail because in luxury the small things are the big things

Apply now , link in bio or DM to connect.

My logo is attached, my web site www.pinecrestbuildworks.com
My style is modern but still warm and inviting. I like a clean classy look .
Updates

Please don’t add any images of chairs or people to the flyer , I do not want people on my flyer. Do not add standard images of offices and houses , we are luxury builders , we build homes over 2 million dollars. Keep a classy , simple modern look . High end .

You can add a white hard hat with my logo on it for a image , this is a suggestion does not have to be on my flyer ,

```html
<!DOCTYPE html>
<html lang="en">
<head>
<meta charset="utf-8">
<title>Pinecrest Buildworks – We're Hiring</title>
<link href="https://fonts.googleapis.com/css2?family=Montserrat:wght@400;500;600;700;800&display=swap" rel="stylesheet">
<style>
  :root{
    --board:#b9b9b9;
    --label-ink:#3d3d3d;
    --label-line:#4a4a4a;
    --paper-top:#f8f8f8;
    --paper-bottom:#e9e9e9;
    --ink-dark:#3a3a3c;
    --ink-brown:#5e5046;
    --ink-body:#4b4140;
    --cta:#5b4b42;
    --band:#625d57;
    --white:#ffffff;
  }
  *{margin:0;padding:0;box-sizing:border-box}
  html,body{width:1200px;height:865px;overflow:hidden}
  body{background:var(--board);font-family:"Montserrat",sans-serif;position:relative}

  .slide-label{position:absolute;top:67px;width:208px;height:42px;border:1px solid var(--label-line);border-radius:21px;
    display:flex;align-items:center;justify-content:center;font-weight:700;font-size:25px;letter-spacing:-0.5px;color:var(--label-ink)}
  .slide-label--one{left:228px}
  .slide-label--two{left:785px}

  .slide{position:absolute;top:169px;width:544px;height:544px;overflow:hidden;
    background:linear-gradient(180deg,var(--paper-top) 0%,var(--paper-bottom) 100%);
    box-shadow:0 22px 22px -14px rgba(0,0,0,.28)}
  .slide--intro{left:44px}
  .slide--requirements{left:607px}

  .wordmark{position:absolute;left:73px;top:60px;color:var(--ink-brown);font-weight:500;font-size:19px;letter-spacing:2px;line-height:1.1;text-transform:uppercase}
  .wordmark::before{content:"";display:inline-block;width:9px;height:9px;border-radius:50%;background:var(--ink-brown);margin-right:8px;vertical-align:2px}

  .footer-band{position:absolute;left:0;bottom:0;width:544px;height:80px}
  .website{position:absolute;right:38px;bottom:25px;color:var(--white);font-weight:600;font-size:12px;letter-spacing:.2px}

  /* Slide 1 */
  .intro-line{position:absolute;left:73px;top:138px;width:340px;color:var(--ink-brown);font-size:14px;line-height:19px;font-weight:400}
  .hiring-title{position:absolute;left:70px;top:216px;color:var(--ink-dark);line-height:1}
  .hiring-title .lead{display:block;font-weight:400;font-size:38px;letter-spacing:-0.5px}
  .hiring-title .main{display:block;font-weight:800;font-size:74px;letter-spacing:-3px;margin-top:-6px}
  .role-pill{position:absolute;left:54px;top:360px;width:249px;height:35px;border:1px solid var(--ink-brown);border-radius:18px;
    display:flex;align-items:center;justify-content:center;font-size:14.5px;color:var(--ink-body)}
  .role-pill strong{font-weight:700;margin-right:4px}
  .role-sub{position:absolute;left:69px;top:400px;font-size:14.5px;color:var(--ink-brown)}
  .apply-card{position:absolute;left:368px;top:314px;width:136px;height:170px;background:var(--cta);border-top-left-radius:32px;
    box-shadow:6px 4px 10px rgba(0,0,0,.18);color:var(--white);padding:24px 0 0 28px}
  .apply-card h2{font-weight:700;font-size:24px;line-height:26px;letter-spacing:-0.5px}
  .apply-card p{margin-top:22px;font-size:11.5px;line-height:14.5px}

  /* Slide 2 */
  .req-title{position:absolute;left:80px;top:123px;font-weight:700;font-size:26px;color:var(--ink-dark);letter-spacing:-0.2px}
  .req-rule{position:absolute;left:79px;top:159px;width:61px;height:1.5px;background:var(--ink-dark)}
  .req-item{position:absolute;left:88px;width:420px;display:flex;gap:5px;font-size:11.6px;line-height:15.5px;color:var(--ink-body)}
  .req-item svg{flex:0 0 10px;width:10px;height:10px;margin-top:3px}
  .req-item .gap{line-height:20.5px}
</style>
</head>
<body>

<div class="slide-label slide-label--one">SLIDE 1</div>
<div class="slide-label slide-label--two">SLIDE 2</div>

<section class="slide slide--intro">
  <div class="wordmark">Pinecrest Buildworks</div>
  <p class="intro-line">Looking For A Construction Project Manager Who’s Passionate About Building Luxury Homes At The Highest Standards</p>
  <h1 class="hiring-title"><span class="lead">We’re</span><span class="main">Hiring</span></h1>
  <div class="role-pill"><strong>Construction</strong> Project Manager</div>
  <div class="role-sub">for Luxury Homes</div>
  <div class="apply-card">
    <h2>Apply<br>Now!</h2>
    <p>link in bio or<br>DM to connect</p>
  </div>
  <svg class="footer-band" viewBox="0 0 544 80" aria-hidden="true">
    <path d="M0 80 C8 60 28 42 51 39 L544 0 L544 80 Z" fill="var(--band)"/>
  </svg>
  <div class="website">www.pinecrestbuildworks.com</div>
</section>

<section class="slide slide--requirements">
  <div class="wordmark">Pinecrest Buildworks</div>
  <h2 class="req-title">Requirements :</h2>
  <div class="req-rule"></div>

  <svg width="0" height="0" style="position:absolute">
    <symbol id="tick" viewBox="0 0 10 10">
      <rect x="0.6" y="0.6" width="8.8" height="8.8" rx="2.4" fill="none" stroke="currentColor" stroke-width="1"/>
      <path d="M2.6 5.1 L4.4 6.8 L9.4 1.4" fill="none" stroke="currentColor" stroke-width="1.1" stroke-linecap="round" stroke-linejoin="round"/>
    </symbol>
  </svg>

  <div class="req-item" style="top:188px"><svg><use href="#tick"/></svg><span>Experience 5+ years in residential project management<br>with a strong portfolio of completed homes.</span></div>
  <div class="req-item" style="top:229px"><svg><use href="#tick"/></svg><span>location : Bergen County, NJ</span></div>
  <div class="req-item" style="top:250px"><svg><use href="#tick"/></svg><span>excellent leadership skills, leads teams with confidence and clarity</span></div>
  <div class="req-item" style="top:271px"><svg><use href="#tick"/></svg><span class="gap">communicates seamlessly with architects , engineers, designers<br>and clients</span></div>
  <div class="req-item" style="top:311px"><svg><use href="#tick"/></svg><span>knows how to manage budgets and timelines without<br>compromising quality</span></div>
  <div class="req-item" style="top:353px"><svg><use href="#tick"/></svg><span>solves problems with a positive solution first mindset</span></div>
  <div class="req-item" style="top:373px"><svg><use href="#tick"/></svg><span>pays attention to every detail because in luxury the small<br>things are the big things</span></div>

  <svg class="footer-band" viewBox="0 0 544 80" aria-hidden="true">
    <path d="M0 80 C8 60 28 42 51 39 L544 0 L544 80 Z" fill="var(--band)"/>
  </svg>
  <div class="website">www.pinecrestbuildworks.com</div>
</section>

</body>
</html>
```